Bright Orbit Care Re-Design\ Add Hosting Content

We are redesigning our web site. We have already picked out the Kestrel WordPress Hosting theme. All content will come from our current website and go onto the new website. http://www.bright-orbit-care.example . This website will interface with WHMCS billing software. I have attached old logos as well as icons for the hosting theme which is also attached.

Target Market(s)

Tech, Web, Hosting

Industry/Entity Type

Tech

Logo Text

Bright Orbit Care, "The New IT Department"

```html
<!DOCTYPE html>
<html lang="en">
<head>
<meta charset="utf-8">
<title>Bright Orbit Care — The New IT Department</title>
<link rel="stylesheet" href="https://fonts.googleapis.com/css2?family=Roboto:wght@300;400;500;700&display=swap">
<style>
:root{
  --red:#c8102e;
  --blue:#4b3ff2;
  --ink:#222;
  --muted:#555;
  --light:#f4f4f4;
  --dark:#1b1b1b;
  --band:#202020;
  --white:#fff;
}
*{box-sizing:border-box;margin:0;padding:0}
html,body{width:1200px;height:3303px;overflow:hidden}
body{font-family:'Roboto',Arial,sans-serif;color:var(--ink);background:var(--white);position:relative}
a{color:inherit;text-decoration:none}

.site-header{height:88px;display:flex;align-items:center;justify-content:space-between;padding:0 96px 0 118px;background:var(--white)}
.brand{display:flex;align-items:center;gap:10px}
.brand-mark{width:44px;height:44px;border-radius:50%;background:var(--blue)}
.brand-name{font-size:21px;font-weight:700;color:var(--blue);line-height:1.05}
.brand-tag{font-size:13px;font-weight:700;color:var(--blue)}
.main-nav{display:flex;gap:14px}
.main-nav a{font-size:14px;padding:6px 16px;color:var(--ink)}
.main-nav a.active{background:var(--blue);color:var(--white)}

.hero{height:473px;position:relative;overflow:hidden;background:linear-gradient(90deg,#2b6fa6 0%,#5fa4d6 40%,#c9dfee 70%,#e7d7cc 100%)}
.hero-copy{position:absolute;left:128px;top:190px;width:360px;color:var(--white)}
.hero-copy h1{font-size:22px;font-weight:400;line-height:1.28}
.btn{display:inline-block;font-size:13px;padding:9px 14px;color:var(--white)}
.btn-red{background:var(--red)}
.btn-blue{background:var(--blue)}
.hero-copy .btn{margin-top:10px}
.hero-dots{position:absolute;left:563px;top:424px;display:flex;gap:8px}
.hero-dots span{width:8px;height:8px;border-radius:50%;background:var(--white)}
.hero-dots span:first-child{background:var(--red)}

.shop-band{height:84px;background:var(--band);display:flex;align-items:center;justify-content:center;gap:44px;color:var(--white);font-size:19px;font-weight:300}
.shop-band em{font-style:normal;color:var(--red)}
.shop-band .btn{font-size:14px;padding:12px 26px}

.section-title{font-size:30px;font-weight:400;color:var(--red);text-align:center}

.offer{height:588px;padding-top:52px}
.offer-grid{display:flex;justify-content:center;margin-top:48px}
.offer-item{width:322px;text-align:center;display:flex;flex-direction:column;align-items:center}
.offer-icon{width:150px;height:143px;border-radius:14px;background:#cfd6de}
.offer-item:nth-child(3) .offer-icon{border-radius:50%;width:143px;background:#e77a2b}
.offer-item h3{font-size:19px;font-weight:400;color:var(--blue);margin-top:34px}
.offer-item p{font-size:11.5px;line-height:1.75;color:var(--muted);width:250px;margin-top:12px;height:100px}
.offer-item .btn{margin-top:20px;font-size:13px;padding:9px 16px}

.hosting{height:777px;background:var(--light);padding-top:81px}
.hosting-grid{display:grid;grid-template-columns:repeat(4,242px);justify-content:center;row-gap:70px;margin-top:54px}
.host-item{text-align:center;display:flex;flex-direction:column;align-items:center}
.host-icon{width:74px;height:76px;border-radius:10px;background:#9aa4ae}
.host-item h4{font-size:14px;font-weight:400;color:#333;margin-top:14px}
.host-item p{font-size:11px;line-height:1.75;color:var(--muted);width:225px;margin-top:10px}

.testimonial{height:421px;background:linear-gradient(180deg,#2a0a0e,#5a0c16 50%,#2a080c);color:var(--white);text-align:center;padding-top:117px}
.testimonial h2{font-size:27px;font-weight:400}
.testimonial blockquote{font-size:15px;line-height:1.7;width:960px;margin:30px auto 0}
.testimonial blockquote::before{content:"\201C";font-size:34px;line-height:0;vertical-align:-8px;margin-right:4px}
.testimonial cite{display:block;font-style:normal;font-size:14px;font-weight:500;margin-top:54px}

.contact-band{height:81px;background:var(--red);display:flex;align-items:center;justify-content:center;gap:44px;color:var(--white);font-size:15.5px;font-weight:500}
.contact-band .btn{font-size:14px;padding:11px 24px}

.consult{height:229px;text-align:center;padding-top:38px}
.consult h2{font-size:44px;font-weight:400;color:var(--red);line-height:1}
.consult h2 b{font-weight:700}
.consult p{font-size:15px;color:#444;margin-top:4px}
.consult-form{display:flex;justify-content:center;gap:6px;margin-top:26px}
.consult-form span{width:258px;height:44px;border:1px solid #e6e6e6;text-align:left;font-size:10px;color:#aaa;padding:15px 10px}
.consult-form .btn{width:136px;height:44px;font-size:14px;line-height:26px;margin-left:4px}

.partners{height:163px;text-align:center;padding-top:35px}
.partners h5{font-size:12px;font-weight:400;letter-spacing:2px;color:#444}
.partner-row{display:flex;justify-content:center;align-items:center;gap:46px;margin-top:36px}
.partner{display:flex;align-items:center;gap:8px;font-size:22px;font-weight:700;color:#333}
.partner i{width:14px;height:14px;background:var(--red);display:block}

.site-footer{height:399px;background:var(--dark);color:#ddd;position:relative}
.foot-col{position:absolute;top:38px;font-size:11px;line-height:1.7}
.foot-col h6{font-size:13px;font-weight:400;color:var(--red);margin-bottom:20px}
.quick-links{left:128px}
.quick-links li{list-style:none;line-height:25px}
.news{left:289px;width:280px}
.news .item{border-top:1px solid #444;padding:8px 0 18px}
.news .item:first-of-type{margin-top:76px}
.news small{display:block;font-size:10px;color:#bbb}
.contact-info{left:610px}
.about{left:852px;width:220px}
.badges{display:flex;gap:12px;margin-top:28px}
.badges span{width:88px;height:32px;background:#3a5d9a}
.badges span+span{background:#cfd6de}
.copyright{position:absolute;left:128px;bottom:18px;font-size:10.5px;color:#bbb}
.social{position:absolute;right:140px;bottom:16px;width:16px;height:16px;background:#3b5b99;border-radius:3px}
</style>
</head>
<body>
<header class="site-header">
  <div class="brand">
    <span class="brand-mark"></span>
    <div>
      <div class="brand-name">Bright Orbit Care</div>
      <div class="brand-tag">"The New IT Department"</div>
    </div>
  </div>
  <nav class="main-nav">
    <a class="active" href="#">Home</a><a href="#">Services</a><a href="#">Business Users</a><a href="#">Home Users</a><a href="#">About Us</a><a href="#">Contact</a>
  </nav>
</header>

<section class="hero" role="img" aria-label="Photo of a smiling support agent wearing a headset in front of a blue office backdrop">
  <div class="hero-copy">
    <h1>We Can Provide Industry Proven Expxertise For yput buiness at a fraction of the cost</h1>
    <a class="btn btn-red" href="#">Learn More</a>
  </div>
  <div class="hero-dots"><span></span><span></span><span></span><span></span><span></span></div>
</section>

<section class="shop-band">
  <p><em>Bright Orbit Care</em> now offers on-line ordering. Visit BOC Shop</p>
  <a class="btn btn-blue" href="#">Find Out More</a>
</section>

<section class="offer">
  <h2 class="section-title">What We Offer</h2>
  <div class="offer-grid">
    <div class="offer-item">
      <div class="offer-icon" role="img" aria-label="Desktop computer monitor illustration"></div>
      <h3>$50 Flat Rate Repair</h3>
      <p>When it comes to business, IT is an absolute must. However, hiring your own IT employees isn't. BOC can provide industry-proven expertise for your business at a fraction of the cost of hiring your own IT support department.</p>
      <a class="btn btn-blue" href="#">Learn More</a>
    </div>
    <div class="offer-item">
      <div class="offer-icon" role="img" aria-label="Server rack illustration"></div>
      <h3>Online Backup</h3>
      <p>DataVault offers you and your business a variety of data backup solutions to fit your specific needs. For non-commercial backup of your personal files, check out the simplicity of DataVault.</p>
      <a class="btn btn-blue" href="#">Learn More</a>
    </div>
    <div class="offer-item">
      <div class="offer-icon" role="img" aria-label="Round orange email sync illustration"></div>
      <h3>Email Solutions</h3>
      <p>Email designed with Business and Home users in mind. Experience a clean, fast Webmail with powerful features for your business and home needs. Learn how our mail solutions can help your business.</p>
      <a class="btn btn-blue" href="#">Learn More</a>
    </div>
  </div>
</section>

<section class="hosting">
  <h2 class="section-title">Our Hosting Services</h2>
  <div class="hosting-grid">
    <div class="host-item"><div class="host-icon" role="img" aria-label="Database icon"></div><h4>Data Backup &amp; Recovery</h4><p>Lorem Ipsum is simply dummy text of the printing and typesetting industry. Lorem Ipsum has been the industry's standard dummy text ever since the 1500s,</p></div>
    <div class="host-item"><div class="host-icon" role="img" aria-label="Crossed tools icon"></div><h4>Repair &amp; Diagnostics</h4><p>Lorem Ipsum is simply dummy text of the printing and typesetting industry. Lorem Ipsum has been the industry's standard dummy text ever since the 1500s,</p></div>
    <div class="host-item"><div class="host-icon" role="img" aria-label="Gauge icon"></div><h4>Virus &amp; Malware Protection</h4><p>Lorem Ipsum is simply dummy text of the printing and typesetting industry. Lorem Ipsum has been the industry's standard dummy text ever since the 1500s,</p></div>
    <div class="host-item"><div class="host-icon" role="img" aria-label="Monitor icon"></div><h4>Updates &amp; Installations</h4><p>Lorem Ipsum is simply dummy text of the printing and typesetting industry. Lorem Ipsum has been the industry's standard dummy text ever since the 1500s,</p></div>
    <div class="host-item"><div class="host-icon" role="img" aria-label="Globe icon"></div><h4>Computer Networking</h4><p>Lorem Ipsum is simply dummy text of the printing and typesetting industry. Lorem Ipsum has been the industry's standard dummy text ever since the 1500s,</p></div>
    <div class="host-item"><div class="host-icon" role="img" aria-label="Envelope icon"></div><h4>Email Setup</h4><p>Lorem Ipsum is simply dummy text of the printing and typesetting industry. Lorem Ipsum has been the industry's standard dummy text ever since the 1500s,</p></div>
    <div class="host-item"><div class="host-icon" role="img" aria-label="Command prompt icon"></div><h4>Windows Troubleshooting</h4><p>Lorem Ipsum is simply dummy text of the printing and typesetting industry. Lorem Ipsum has been the industry's standard dummy text ever since the 1500s,</p></div>
    <div class="host-item"><div class="host-icon" role="img" aria-label="Computer tower icon"></div><h4>Optimizing Computer Speed</h4><p>Lorem Ipsum is simply dummy text of the printing and typesetting industry. Lorem Ipsum has been the industry's standard dummy text ever since the 1500s,</p></div>
  </div>
</section>

<section class="testimonial" role="img" aria-label="Dark red tinted photo of a server room aisle behind the client quote">
  <h2>What Our Clients Say</h2>
  <blockquote>After a competitive bid review, we contracted with Bright Orbit Care to be our IT Department Network Administrator. BOC is a collaborative partner that has met our expectations. We trust our computers and / or network are in good hands with Bright Orbit Care. We are spending less and have shortened our system down time.</blockquote>
  <cite>Ray K&amp;M Electric (Riverton, NE)</cite>
</section>

<section class="contact-band">
  <p>Contact a Bright Orbit Care professional in Riverton today at (555) 014-2290 or info@bright-orbit-care.example</p>
  <a class="btn btn-blue" href="#">Contact Us</a>
</section>

<section class="consult">
  <h2><b>Free</b> Consultations</h2>
  <p>Receive a FREE Consultation Now!</p>
  <div class="consult-form">
    <span>Your Name (Required)</span><span>Your Email (Required)</span><span>Phone</span>
    <a class="btn btn-red" href="#">Send</a>
  </div>
</section>

<section class="partners">
  <h5>Our Partners</h5>
  <div class="partner-row">
    <span class="partner">Wardline</span>
    <span class="partner">Solvant</span>
    <span class="partner">Mirafield</span>
    <span class="partner"><i></i>Helixa</span>
    <span class="partner">Dunlink</span>
    <span class="partner">VoltaCore</span>
  </div>
</section>

<footer class="site-footer">
  <div class="foot-col quick-links">
    <h6>Quick Links</h6>
    <ul>
      <li>About Bright Orbit Care</li><li>Our Partners</li><li>Terms &amp; Conditions</li><li>Privacy Policy</li><li>Certifications</li><li>Testimonials</li><li>News</li><li>Security Alerts</li><li>Contact Us</li><li>Sitemap</li>
    </ul>
  </div>
  <div class="foot-col news">
    <h6>Recent News</h6>
    <div class="item"><small>May 27, 2014</small>You Have a Computer Virus – Now What?</div>
    <div class="item"><small>May 27, 2014</small>Protecting Your Home Computer from Data Loss</div>
  </div>
  <div class="foot-col contact-info">
    <h6>Contact Us</h6>
    <p>Bright Orbit Care, LLC<br>1200 Harbor Lane, Ste 101<br>Riverton, Nebraska 00000<br>(555) 014-2290</p>
    <p style="margin-top:12px">info@bright-orbit-care.example<br>http://www.bright-orbit-care.example</p>
  </div>
  <div class="foot-col about">
    <h6>About Us</h6>
    <p>At Bright Orbit Care, we began our company with the idea of providing superior online technical support, affordable computer repair, and managed service solutions to businesses and home consumers, using the best practices and technology in the industry, for the least cost.</p>
    <div class="badges"><span></span><span></span></div>
  </div>
  <p class="copyright">© Copyright - 2014 Bright Orbit Care, LLC. All Rights Reserved.</p>
  <span class="social"></span>
</footer>
</body>
</html>
```